An anniversary gift for my girlfriend

My girlfriend and I have been dating for almost 2 years. We met online and this has afforded us the really unique opportunity to have the first words we said to each other (the whole conversation, in fact) preserved. We're moving in together in a few months and she doesn't know that I saved the conversation. I've been waiting for this to turn it into something we can hang in our new place.

The only phrase I want to use is:
"Well if you dislike people's knees then I think we'll get along famously"

It's an Nobody Leaves Before Midnight in Portland reference for the curious.

I want the poster to use the words themselves as the art; I'm thinking typography. I'd like it to match her aesthetic, she likes to wear Nora Vell and T. Brisk. Colors shouldn't be anything too "girly". Somewhere I'd like to include the date June 1, 2015. It shouldn't be a major piece of the poster though, just a way to denote the date.

It should fit (and be fully visible in) a 16x20 (inches) frame

Thanks in advance for the work!

Requirements
Must have
• Must use only the words: "Well if you dislike people's knees then I think we'll get along famously"
• I want this to be typography, so making the phrase the center of the poster and the art itself.

```html
<!DOCTYPE html>
<html lang="en">
<head>
<meta charset="utf-8">
<title>Well if you dislike people's knees — anniversary poster</title>
<link rel="stylesheet" href="https://fonts.googleapis.com/css2?family=Jost:wght@400&display=swap">
<style>
  :root {
    --ink: #f6f3c4;
    --accent: #b3265c;
    --night: #0d0e10;
    --key: #1c1d20;
  }
  html, body {
    margin: 0;
    padding: 0;
    width: 738px;
    height: 1200px;
    overflow: hidden;
    background: var(--night);
  }
  .poster {
    position: relative;
    width: 738px;
    height: 1200px;
    overflow: hidden;
  }
  .backdrop {
    position: absolute;
    inset: 0;
    background:
      radial-gradient(ellipse at 45% 45%, var(--key) 0%, #141517 45%, var(--night) 100%);
  }
  .phrase {
    position: absolute;
    inset: 0;
  }
  .word {
    font-family: "Jost", "Futura", "Century Gothic", sans-serif;
    font-weight: 400;
    fill: var(--ink);
  }
  .rule { fill: var(--ink); }
  .date {
    font-family: "Jost", "Futura", "Century Gothic", sans-serif;
    font-weight: 400;
    fill: var(--accent);
  }
</style>
</head>
<body>
<main class="poster">
  <div class="backdrop" role="img" aria-label="Dark close-up photograph of black computer keyboard keys"></div>

  <svg class="phrase" width="738" height="1200" viewBox="0 0 738 1200" xmlns="http://www.w3.org/2000/svg" aria-label="Well if you dislike people's knees then I think we'll get along famously">
    <!-- guide strokes -->
    <rect class="rule rule-top" x="345" y="0" width="4" height="322"/>
    <rect class="rule rule-left" x="240" y="318" width="4" height="138"/>
    <rect class="rule rule-then" x="405" y="478" width="4" height="172"/>
    <rect class="rule rule-long" x="465" y="425" width="4" height="775"/>

    <text class="word word-well" x="255" y="228" font-size="56" textLength="110" lengthAdjust="spacingAndGlyphs">well</text>
    <text class="word word-if-you" x="188" y="306" font-size="74" textLength="194" lengthAdjust="spacingAndGlyphs">if you</text>
    <text class="word word-dislike" x="262" y="372" font-size="54" textLength="148" lengthAdjust="spacingAndGlyphs">dislike</text>
    <text class="word word-peoples" x="262" y="410" font-size="54" textLength="220" lengthAdjust="spacingAndGlyphs">people's</text>
    <text class="word word-knees" transform="translate(540 420) rotate(-90)" font-size="54" textLength="146" lengthAdjust="spacingAndGlyphs">knees</text>

    <text class="word word-then" x="188" y="506" font-size="94" textLength="222" lengthAdjust="spacingAndGlyphs">then</text>
    <text class="word word-think" transform="translate(245 656) rotate(-90)" font-size="52" textLength="126" lengthAdjust="spacingAndGlyphs">think</text>
    <text class="word word-well-contraction" x="258" y="590" font-size="52" textLength="127" lengthAdjust="spacingAndGlyphs">we'll</text>
    <text class="word word-get" x="290" y="627" font-size="52" textLength="95" lengthAdjust="spacingAndGlyphs">get</text>

    <text class="word word-along" x="260" y="746" font-size="106" textLength="282" lengthAdjust="spacingAndGlyphs">along</text>
    <text class="word word-famously" x="245" y="810" font-size="56" textLength="265" lengthAdjust="spacingAndGlyphs">famously</text>

    <text class="date" transform="translate(460 1110) rotate(-90)" font-size="40" textLength="206" lengthAdjust="spacingAndGlyphs">6.01.2015</text>
  </svg>
</main>
</body>
</html>
```